Digital Marketing Brochure - PDF

I am seeking to have a digital marketing brochure consistent with our webpage of birchwellgroup.com that includes our staff, territory and will have available links to a share file for our insurance documents and rates, etc. - I have uploaded our logo and would like you work with our webpage to keep consistent. We would like this to be a pdf style document that reads like a book and has pleasing modern, rustic appearance consistent with our web page.

Target Market(s)

Insurance companies

Industry/Entity Type

Insurance

Requirements
Must have
• Flip through marketing brochure. Essentially want it to be our webpage in a e-mailable or downloadable pdf.

```html
<!DOCTYPE html>
<html lang="en">
<head>
<meta charset="utf-8">
<title>Birchwell Claims Brochure</title>
<link rel="stylesheet" href="https://fonts.googleapis.com/css2?family=Montserrat:ital,wght@0,400;0,600;0,800;1,500&family=Open+Sans:ital,wght@0,400;0,600;0,700;1,400&family=Roboto+Condensed:wght@400&family=Kaushan+Script&display=swap">
<style>
:root{
  --navy:#123a7c;
  --navy-deep:#0b2a63;
  --orange:#f07a22;
  --orange-soft:#f39a4e;
  --paper:#f3f4f6;
  --ink:#2b2f38;
  --stage:#e6e6e8;
}
*{box-sizing:border-box;margin:0;padding:0}
html,body{width:947px;height:1200px;overflow:hidden;background:var(--stage)}
body{position:relative;font-family:"Open Sans",sans-serif;color:var(--ink)}
.spread{position:absolute;left:23px;width:900px;height:560px;display:flex;box-shadow:0 6px 18px rgba(0,0,0,.18)}
.spread--covers{top:25px}
.spread--inside{top:615px}
.page{position:relative;width:450px;height:560px;overflow:hidden;background:var(--paper)}
.page--blue{background:linear-gradient(160deg,#1a4a95 0%,var(--navy) 45%,var(--navy-deep) 100%)}

.wordmark{font-family:"Montserrat",sans-serif;font-weight:800;color:var(--orange);letter-spacing:1px;line-height:1}
.tagline{font-family:"Montserrat",sans-serif;font-size:7px;letter-spacing:.6px;text-transform:uppercase;color:#fff}

/* footer band */
.footer{position:absolute;left:0;bottom:0;width:100%;height:34px}
.footer svg{position:absolute;inset:0}
.footer__url{position:absolute;bottom:7px;left:0;width:100%;text-align:center;font-family:"Montserrat",sans-serif;font-size:8px;letter-spacing:2px;color:#fff}
.footer__url::before{content:"";display:inline-block;width:7px;height:7px;border-radius:50%;background:#fff;margin-right:6px;vertical-align:-1px}

/* back cover */
.back-brand{position:absolute;top:205px;width:100%;text-align:center}
.back-brand .wordmark{font-size:46px}
.contact-title{position:absolute;top:285px;width:100%;text-align:center;font-family:"Montserrat",sans-serif;font-weight:800;font-size:17px;color:#fff}
.contact-icons{position:absolute;top:318px;width:100%;display:flex;justify-content:center;gap:8px}
.contact-icons span{width:14px;height:14px;border-radius:50%;background:var(--orange);display:flex;align-items:center;justify-content:center}
.contact-lines{position:absolute;top:342px;width:100%;text-align:center;font-family:"Montserrat",sans-serif;font-size:9px;line-height:1.45;color:#fff;text-transform:uppercase}
.contact-lines p+p{margin-top:8px}

/* front cover */
.front-head{position:absolute;top:0;left:0;width:100%;height:95px;background:linear-gradient(180deg,#1a4a95,var(--navy))}
.front-head .brand{position:absolute;top:26px;width:100%;text-align:center}
.front-head .wordmark{font-size:38px}
.front-glass{position:absolute;top:70px;right:0;width:120px;height:330px;background:linear-gradient(180deg,rgba(200,210,225,.6),rgba(225,230,238,.3));clip-path:polygon(35% 0,100% 0,100% 100%,0 100%)}
.front-photo{position:absolute;top:95px;left:48px;width:402px;height:155px;background:linear-gradient(110deg,#5a3e26 0%,#9a5422 35%,#e0701e 65%,#d9531a 100%)}
.front-ribbon{position:absolute;top:250px;left:48px;width:270px;height:80px;background:var(--orange)}
.badges{position:absolute;top:8px;left:0;width:100%;display:flex;justify-content:space-around;padding:0 18px}
.badges span{width:30px;height:30px;border-radius:50%;background:#fff;display:flex;align-items:center;justify-content:center}
.badge-labels{position:absolute;top:48px;width:100%;text-align:center;font-family:"Roboto Condensed",sans-serif;font-size:9.5px;color:#fff}
.front-title{position:absolute;top:385px;left:40px;font-family:"Montserrat",sans-serif;font-weight:800;font-size:30px;color:var(--navy-deep)}
.front-strip{position:absolute;top:421px;left:40px;width:370px;height:14px;background:var(--orange);font-family:"Montserrat",sans-serif;font-weight:600;font-size:7px;color:#fff;text-align:center;line-height:14px;text-transform:uppercase;letter-spacing:.3px}

/* inside left */
.inside-head{position:absolute;top:0;left:0;width:100%;height:110px;background:linear-gradient(180deg,#1a4a95,var(--navy))}
.inside-head .brand{position:absolute;top:26px;width:100%;text-align:center}
.inside-head .wordmark{font-size:34px}
.inside-panel{position:absolute;top:95px;left:28px;width:394px;height:430px;background:var(--paper)}
.why-title{text-align:center;font-family:"Montserrat",sans-serif;font-weight:800;font-size:26px;color:var(--navy-deep);margin-top:10px}
.intro{margin:12px 18px 0;border-left:3px solid var(--orange);padding-left:8px;font-size:8px;line-height:1.45;font-style:italic}
.intro b,.closing b{font-style:normal;color:var(--navy-deep)}
.peril-icons{display:flex;justify-content:center;gap:18px;margin:12px 0 10px}
.points{list-style:none;margin:0 18px;font-size:7.6px;line-height:1.45}
.points li{position:relative;padding-left:10px;margin-bottom:9px}
.points li::before{content:"";position:absolute;left:0;top:4px;width:4px;height:4px;background:var(--orange);transform:rotate(45deg)}
.points strong{color:var(--orange);font-family:"Montserrat",sans-serif;font-weight:800;text-transform:uppercase;font-size:7.6px}
.points p+p{margin-top:6px}
.signoff{text-align:center;font-family:"Kaushan Script",cursive;font-size:19px;color:var(--navy);margin-top:6px}

/* inside right */
.right-brand{position:absolute;top:35px;width:100%;text-align:center}
.right-brand .wordmark{font-size:32px}
.right-brand .tagline{color:var(--navy-deep);font-size:6px}
.right-title{position:absolute;top:80px;width:100%;text-align:center;font-family:"Montserrat",sans-serif;font-weight:800;font-size:15px;line-height:1.25;color:var(--navy-deep)}
.right-glass{position:absolute;top:120px;right:0;width:110px;height:210px;background:rgba(200,210,225,.55)}
.right-photo{position:absolute;top:125px;left:95px;width:355px;height:195px;background:linear-gradient(180deg,#c7cacd 0%,#a3a8a6 45%,#6e736f 75%,#55585b 100%)}
.service-card{position:absolute;top:195px;left:40px;width:230px;height:120px;background:var(--orange);transform:skewY(-6deg);padding:38px 28px 0}
.service-card p{transform:skewY(6deg);text-align:center;color:#fff;font-size:8px;line-height:1.5}
.service-pin{position:absolute;top:172px;left:138px;width:40px;height:40px;border-radius:50%;background:#fff;border:5px solid var(--navy);display:flex;align-items:center;justify-content:center}
.phone-icon{position:absolute;top:355px;left:140px;width:26px;height:26px;border-radius:50%;border:1.5px solid var(--orange);display:flex;align-items:center;justify-content:center}
.phone-number{position:absolute;top:390px;left:80px;font-family:"Montserrat",sans-serif;font-style:italic;font-weight:500;font-size:20px;color:var(--navy-deep)}
.closing{position:absolute;top:425px;left:80px;width:320px;font-size:8px;line-height:1.5;text-align:justify}
</style>
</head>
<body>

<section class="spread spread--covers">
  <article class="page page--blue page--back">
    <div class="back-brand">
      <div class="wordmark">BIRCHWELL</div>
      <div class="tagline">Birchwell Claims &amp; Adjusting Services</div>
    </div>
    <h2 class="contact-title">CONTACT US</h2>
    <div class="contact-icons">
      <span><svg width="8" height="8" viewBox="0 0 10 10"><path d="M5 0a3.5 3.5 0 0 0-3.5 3.5C1.5 6 5 10 5 10s3.5-4 3.5-6.5A3.5 3.5 0 0 0 5 0z" fill="#fff"/></svg></span>
      <span><svg width="8" height="8" viewBox="0 0 10 10"><path d="M2 1l2 2-1 1.5a6 6 0 0 0 2.5 2.5L7 6l2 2-1.5 1.5C4 9 1 6 .5 2.5z" fill="#fff"/></svg></span>
      <span><svg width="8" height="8" viewBox="0 0 10 10"><rect x="1" y="4" width="8" height="5" fill="#fff"/><rect x="3" y="1" width="4" height="3" fill="#fff"/></svg></span>
    </div>
    <div class="contact-lines">
      <p>PO Box 210 48 Millbrook Lane<br>Hollis Bay, NY 12990</p>
      <p>Phone: 555-014-2290<br>Fax: 555-017-4836</p>
      <p>1-800-555-0142</p>
    </div>
    <footer class="footer">
      <svg width="450" height="34" viewBox="0 0 450 34"><polygon points="0,8 120,8 110,14 0,14" fill="var(--orange)"/><polygon points="330,8 450,8 450,14 340,14" fill="var(--orange)"/><rect y="14" width="450" height="20" fill="var(--navy-deep)"/></svg>
      <div class="footer__url">www.birchwellgroup.com</div>
    </footer>
  </article>

  <article class="page page--front">
    <header class="front-head">
      <div class="brand">
        <div class="wordmark">BIRCHWELL</div>
        <div class="tagline">Birchwell Claims &amp; Adjusting Services</div>
      </div>
    </header>
    <div class="front-glass"></div>
    <div class="front-photo" role="img" aria-label="Photo: firefighters in protective gear tackling a large blaze"></div>
    <div class="front-ribbon">
      <div class="badges">
        <span><svg width="16" height="16" viewBox="0 0 16 16"><circle cx="8" cy="8" r="6" fill="none" stroke="var(--navy)" stroke-width="1.5"/><path d="M8 4v4l3 2" stroke="var(--navy)" stroke-width="1.5" fill="none"/></svg></span>
        <span><svg width="16" height="16" viewBox="0 0 16 16"><rect x="3" y="2" width="10" height="12" fill="none" stroke="var(--navy)" stroke-width="1.5"/><path d="M5 6h6M5 9h6M5 12h4" stroke="var(--orange)" stroke-width="1.2"/></svg></span>
        <span><svg width="16" height="16" viewBox="0 0 16 16"><circle cx="8" cy="7" r="5" fill="var(--navy)"/><path d="M5 11l-1 4 4-2 4 2-1-4" fill="var(--navy)"/></svg></span>
      </div>
      <div class="badge-labels">24/7 Claim Service &nbsp;|&nbsp; Fast Reporting &nbsp;|&nbsp; Premium Quality</div>
    </div>
    <h1 class="front-title">WHEN IT HAPPENS</h1>
    <div class="front-strip">Accidents, disasters, fire, flood, wind, property &amp; liability</div>
    <footer class="footer">
      <svg width="450" height="34" viewBox="0 0 450 34"><polygon points="0,8 120,8 110,14 0,14" fill="var(--orange)"/><polygon points="330,8 450,8 450,14 340,14" fill="var(--orange)"/><rect y="14" width="450" height="20" fill="var(--navy-deep)"/></svg>
      <div class="footer__url">www.birchwellgroup.com</div>
    </footer>
  </article>
</section>

<section class="spread spread--inside">
  <article class="page page--why">
    <header class="inside-head">
      <div class="brand">
        <div class="wordmark">BIRCHWELL</div>
        <div class="tagline">Birchwell Claims &amp; Adjusting Services</div>
      </div>
    </header>
    <div class="inside-panel">
      <h2 class="why-title">WHY BIRCHWELL</h2>
      <p class="intro"><b>BIRCHWELL</b> retains the benefits of a large firm in our capacity to handle high volume and complex claims over a large geographical area while at the same time retaining flexibility and personal tailored service.</p>
      <div class="peril-icons">
        <svg width="22" height="20" viewBox="0 0 22 20"><path d="M5 10a5 5 0 0 1 5-6 5 5 0 0 1 8 3 3 3 0 0 1 0 6H5a3 3 0 0 1 0-6z" fill="var(--navy)"/><path d="M9 14l-2 5M14 14l-2 5" stroke="var(--navy)" stroke-width="1.5"/></svg>
        <svg width="20" height="20" viewBox="0 0 20 20"><path d="M10 2l8 7h-2v9H4V9H2z" fill="var(--navy)"/><rect x="8" y="12" width="4" height="6" fill="#fff"/></svg>
        <svg width="24" height="20" viewBox="0 0 24 20"><path d="M4 8a8 6 0 0 1 16 0z" fill="var(--navy)"/><path d="M12 8v4" stroke="var(--navy)"/><rect x="2" y="13" width="20" height="4" rx="2" fill="var(--navy)"/></svg>
        <svg width="22" height="20" viewBox="0 0 22 20"><circle cx="6" cy="6" r="3" fill="var(--navy)"/><circle cx="16" cy="6" r="3" fill="var(--navy)"/><circle cx="11" cy="9" r="3" fill="var(--navy)"/><path d="M4 20a7 7 0 0 1 14 0z" fill="var(--navy)"/></svg>
        <svg width="22" height="20" viewBox="0 0 22 20"><path d="M9 3l8 7h-2v9H3v-9H1z" fill="var(--navy)"/><path d="M17 4c3 3 3 7 0 9-2-2-1-5 0-9z" fill="var(--navy)"/></svg>
        <svg width="22" height="20" viewBox="0 0 22 20"><rect x="4" y="4" width="10" height="14" fill="var(--navy)"/><path d="M2 4h16" stroke="var(--navy)" stroke-width="2"/><path d="M1 16q5-3 10 0t10 0" stroke="var(--navy)" stroke-width="1.5" fill="none"/></svg>
      </div>
      <ul class="points">
        <li><p><strong>Our Staff</strong> - Our most important asset. We pride ourselves in having only the most qualified, self-motivated, trained professionals on our claim team. Our adjusting staff boasts an average experience level of over 20 years. Each of our adjusters takes advantage of the educational and training opportunities afforded to them to improve their skills and obtain industry specific designations.</p><p>Our support staff provides experienced and knowledgeable service, which enhances and assures a smooth workflow for your claim assignment from start to finish.</p></li>
        <li><strong>Our Directive</strong> - Setting the standard for commitment, quality and professionalism. Providing quality, timely professional services to our clients. Our supervision and quality control enables us to consistently deliver a superior product.</li>
        <li><strong>Technology</strong> - Staying on the cutting edge of the new and improved products and equipment required to perform our service professionally and efficiently.</li>
        <li><strong>Our Locations</strong> - With 12 locations throughout the North East we are able to service all of New York State as well as servicing Vermont, Western Massachusetts, Connecticut, Northern New Jersey and Pennsylvania.</li>
      </ul>
      <p class="signoff">Committed to satisfying your needs.</p>
    </div>
    <footer class="footer">
      <svg width="450" height="34" viewBox="0 0 450 34"><polygon points="0,8 120,8 110,14 0,14" fill="var(--orange)"/><polygon points="330,8 450,8 450,14 340,14" fill="var(--orange)"/><rect y="14" width="450" height="20" fill="var(--navy-deep)"/></svg>
      <div class="footer__url">www.birchwellgroup.com</div>
    </footer>
  </article>

  <article class="page page--services">
    <div class="right-brand">
      <div class="wordmark">BIRCHWELL</div>
      <div class="tagline">Birchwell Claims &amp; Adjusting Services</div>
    </div>
    <h2 class="right-title">INDEPENDENT CLAIM<br>ADJUSTERS &amp; ADMINISTRATION</h2>
    <div class="right-glass"></div>
    <div class="right-photo" role="img" aria-label="Photo: overturned car on a roadside after an accident"></div>
    <div class="service-card"><p>Serving you from over 12 locations throughout the North East, with claim adjusters throughout the region, BIRCHWELL has the resources to respond to your adjustment needs.</p></div>
    <div class="service-pin"><svg width="14" height="16" viewBox="0 0 10 12"><path d="M5 .5A4 4 0 0 0 1 4.5C1 7.5 5 11.5 5 11.5s4-4 4-7A4 4 0 0 0 5 .5z" fill="none" stroke="var(--orange)" stroke-width="1.2"/><circle cx="5" cy="4.5" r="1.4" fill="var(--orange)"/></svg></div>
    <div class="phone-icon"><svg width="12" height="12" viewBox="0 0 10 10"><path d="M2 1l2 2-1 1.5a6 6 0 0 0 2.5 2.5L7 6l2 2-1.5 1.5C4 9 1 6 .5 2.5z" fill="none" stroke="var(--orange)" stroke-width="1"/></svg></div>
    <div class="phone-number">1.800.555.0142</div>
    <p class="closing">At <b>BIRCHWELL</b> we take pride in our staff to deliver quality and professional service. We take care of your needs with rapid response and timely reporting, while providing your customers the care and empathy they deserve to help them through their loss.</p>
    <footer class="footer">
      <svg width="450" height="34" viewBox="0 0 450 34"><polygon points="0,8 120,8 110,14 0,14" fill="var(--orange)"/><polygon points="330,8 450,8 450,14 340,14" fill="var(--orange)"/><rect y="14" width="450" height="20" fill="var(--navy-deep)"/></svg>
      <div class="footer__url">www.birchwellgroup.com</div>
    </footer>
  </article>
</section>

</body>
</html>
```